Etiketten-Design für neue Biermarke
Zielgruppe
Es soll eine neue Biermarke entwickelt werden. Die drei grundlegenden Sorten sind: Pils, Radler, Helles. Für die neue Biermarke soll ein Markenname, ein Logo und ein Etikettendesign gestaltet werden. Das Bier soll traditionell sein und den typischen Biertrinker ansprechen. Die Zielgruppe der Biermarke ist die breite Masse. Das Bier soll für 9,90€ verkauft werden.
Aufgabenstellung
Das Design der Etiketten sollte klassisch und traditionell wirken. Es dürfen gerne klassische, historische und urige Elemente wie Hopfen, Bierfass, altertümliche Illustrationen, etc. verwendet werden. Das Bier sollte weder in Richtung eines Craft Bieres noch in die Richtung eines jungen/hippen Bieres gehen.

```html
<!DOCTYPE html>
<html lang="de">
<head>
<meta charset="utf-8">
<title>Altenfels Pilsner – Helles Etikett</title>
<link rel="stylesheet" href="https://fonts.googleapis.com/css2?family=Playfair+Display:wght@400;700;900&family=Pacifico&display=swap">
<style>
  :root {
    --bg: #ffffff;
    --rim: #c0904e;
    --rim-light: #d0a767;
    --field: #dccd8b;
    --field-faint: #e4d89f;
    --ink: #3d1a0e;
    --emblem-top: #7a4a2e;
    --emblem-bottom: #3b1a0c;
    --grain: #c39654;
    --ribbon: #b3121c;
    --ribbon-dark: #8e0d15;
    --ribbon-text: #ffffff;
  }
  html, body {
    margin: 0;
    padding: 0;
    width: 1022px;
    height: 1200px;
    overflow: hidden;
    background: var(--bg);
  }
  .label {
    display: block;
    width: 1022px;
    height: 1200px;
  }
  .label__rim { fill: var(--rim); }
  .label__rim-highlight { fill: var(--rim-light); }
  .label__field { fill: var(--field); }
  .label__barrel { fill: var(--field-faint); }
  .label__tagline {
    font-family: "Playfair Display", serif;
    font-weight: 700;
    font-size: 9.5px;
    letter-spacing: 0.6px;
    fill: var(--ink);
  }
  .label__brand {
    font-family: "Playfair Display", serif;
    font-weight: 900;
    font-size: 56px;
    letter-spacing: 2px;
    fill: var(--ink);
  }
  .label__variety {
    font-family: "Playfair Display", serif;
    font-weight: 900;
    font-size: 70px;
    letter-spacing: 3px;
    fill: var(--ink);
  }
  .label__year {
    font-family: "Playfair Display", serif;
    font-weight: 400;
    font-size: 32px;
    fill: var(--ink);
  }
  .label__grain { fill: var(--grain); }
  .label__emblem { fill: url(#emblem-tone); }
  .ribbon__tail { fill: var(--ribbon-dark); }
  .ribbon__band { fill: var(--ribbon); }
  .ribbon__text {
    font-family: "Pacifico", cursive;
    font-size: 40px;
    fill: var(--ribbon-text);
  }
</style>
</head>
<body>
<svg class="label" viewBox="0 0 620 730" preserveAspectRatio="xMidYMid meet" xmlns="http://www.w3.org/2000/svg">
  <defs>
    <path id="tagline-arc" d="M88,300 A224,255 0 0 1 532,300"/>
    <path id="brand-arc" d="M140,300 A175,180 0 0 1 480,300"/>
    <path id="variety-arc" d="M140,515 Q310,720 480,515"/>
    <linearGradient id="emblem-tone" x1="0" y1="0" x2="0" y2="1">
      <stop offset="0" stop-color="var(--emblem-top)"/>
      <stop offset="1" stop-color="var(--emblem-bottom)"/>
    </linearGradient>
  </defs>

  <ellipse class="label__rim" cx="310" cy="358" rx="264" ry="318"/>
  <ellipse class="label__rim-highlight" cx="310" cy="352" rx="256" ry="308"/>
  <ellipse class="label__field" cx="310" cy="360" rx="250" ry="302"/>

  <text class="label__tagline">
    <textPath href="#tagline-arc" startOffset="50%" text-anchor="middle">NACH DEUTSCHER BRAUQUALITÄT · NACH DEUTSCHER BRAUQUALITÄT · NACH DEUTSCHER BRAUQUALITÄT</textPath>
  </text>

  <text class="label__brand">
    <textPath href="#brand-arc" startOffset="50%" text-anchor="middle">ALTENFELS</textPath>
  </text>

  <rect class="label__barrel" x="202" y="228" width="216" height="232" rx="70" role="img" aria-label="Blasses Bierfass als Hintergrund"/>

  <rect class="label__emblem" x="220" y="256" width="182" height="252" rx="22" role="img" aria-label="Illustration: brüllender Löwe auf einem Felsen"/>

  <rect class="label__grain" x="120" y="322" width="44" height="148" rx="22" role="img" aria-label="Ähren-Ornament"/>
  <rect class="label__grain" x="456" y="322" width="44" height="148" rx="22" role="img" aria-label="Ähren-Ornament"/>

  <text class="label__year" x="72" y="410">18</text>
  <text class="label__year" x="510" y="410">97</text>

  <text class="label__variety">
    <textPath href="#variety-arc" startOffset="50%" text-anchor="middle">PILSNER</textPath>
  </text>

  <path class="ribbon__tail" d="M112,614 L150,622 L150,672 L100,676 L120,646 Z"/>
  <path class="ribbon__tail" d="M508,614 L470,622 L470,672 L520,676 L500,646 Z"/>
  <path class="ribbon__band" d="M128,606 Q310,640 492,606 L496,688 Q310,712 124,688 Z"/>
  <text class="ribbon__text" x="310" y="683" text-anchor="middle">Helles</text>
</svg>
</body>
</html>
```